Kelmora Legal Business Card

I require a corporate business card for a new legal services business.

I do not have a logo, nor do I want one.

I require a clean, neat a professional card for a law firm.

Details:

Business Name: Kelmora Legal
Name: Debra Lindqvist
Title: Corporate Services Manager
Location: Office 14 (Top Floor), Toravel Business Centre, Quinlan Grove Street, Alotau CBD, Milne Bay Province.
Postal Address: PO Box 593, Alotau, 211, Milne Bay Province, Papua New Guinea.
Contact: T: +675 6418250, F: +675 6413362, M: +675 72915867, E: dlindqvist@kelmoraexample.com.pg.

I look forward to your design submissions.

Industry/Entity Type

Legal

```html
<!DOCTYPE html>
<html lang="en">
<head>
<meta charset="utf-8">
<title>Kelmora Legal — Business Card</title>
<link rel="stylesheet" href="https://fonts.googleapis.com/css2?family=Arimo:wght@400;700&display=swap">
<style>
  :root {
    --page-bg: #e9e9e9;
    --card-bg: #f4f4f4;
    --band-red: #8b1519;
    --band-text: #ffffff;
    --ink: #222222;
    --ink-soft: #8a8a8a;
    --label-blue: #3a63b8;
  }
  * { margin: 0; padding: 0; box-sizing: border-box; }
  html, body {
    width: 1200px;
    height: 900px;
    overflow: hidden;
    background: var(--page-bg);
    font-family: "Arimo", Arial, sans-serif;
  }
  .stage {
    width: 1200px;
    height: 900px;
    display: flex;
    align-items: center;
    justify-content: center;
  }
  .business-card {
    position: relative;
    width: 840px;
    height: 500px;
    background: var(--card-bg);
    box-shadow: 0 8px 24px rgba(0, 0, 0, 0.12);
  }
  .brand-band {
    position: absolute;
    top: 58px;
    left: 70px;
    right: 0;
    height: 66px;
    background: var(--band-red);
    display: flex;
    align-items: center;
    justify-content: center;
  }
  .brand-name {
    color: var(--band-text);
    font-size: 38px;
    font-weight: 400;
    letter-spacing: 0.5px;
  }
  .card-details {
    position: absolute;
    top: 148px;
    left: 70px;
    right: 0;
    text-align: center;
    color: var(--ink);
  }
  .person-name {
    font-size: 26px;
    font-weight: 700;
    line-height: 1.15;
  }
  .person-title {
    font-size: 17px;
    color: var(--ink-soft);
    margin-bottom: 22px;
  }
  .address-block,
  .postal-block {
    font-size: 18px;
    line-height: 1.45;
  }
  .postal-block { margin-top: 28px; }
  .contact-label { color: var(--label-blue); }
  .divider { color: var(--ink-soft); padding: 0 6px; }
  .email {
    margin-top: 24px;
    font-size: 18px;
  }
</style>
</head>
<body>
  <main class="stage">
    <article class="business-card">
      <header class="brand-band">
        <h1 class="brand-name">Kelmora Legal</h1>
      </header>
      <section class="card-details">
        <p class="person-name">Debra Lindqvist</p>
        <p class="person-title">Corporate Services Manager</p>
        <address class="address-block">
          Office 14 (Top Floor), Toravel Business Centre<br>
          Quinlan Grove Street, Alotau CBD,<br>
          Milne Bay Province
        </address>
        <div class="postal-block">
          <p>PO Box 593, Alotau, 211, Milne Bay Province, Papua New Guinea</p>
          <p>
            <span class="contact-label">t.</span> +675 6418250<span class="divider">|</span><span class="contact-label">f.</span> +675 6413362<span class="divider">|</span><span class="contact-label">m.</span> +675 72915867
          </p>
        </div>
        <p class="email">dlindqvist@kelmoraexample.com.pg</p>
      </section>
    </article>
  </main>
</body>
</html>
```